Cloud-based vaccination website

Basic website design for cloud-based medical company

Coding

Coded - Design and coding required

Number of Pages Required

1 page

Colors
3277b5

```html
<!DOCTYPE html>
<html lang="en">
<head>
<meta charset="utf-8">
<title>NUVAXA – Cloud-Based Vaccination</title>
<link href="https://fonts.googleapis.com/css2?family=Oswald:wght@300;400;500&family=Poppins:wght@300;400&display=swap" rel="stylesheet">
<style>
:root{
  --blue:#4d72fb;
  --blue-dark:#3252d6;
  --teal:#6fd9c5;
  --ink:#222;
  --text:#555;
  --muted:#9a9a9a;
  --gray-bg:#f5f5f5;
  --footer:#4b4b4b;
  --gold:#f5b400;
  --white:#fff;
}
*{margin:0;padding:0;box-sizing:border-box}
html,body{width:1200px;height:3217px;overflow:hidden}
body{position:relative;background:var(--white);font-family:'Poppins',sans-serif;color:var(--text)}
.abs{position:absolute}
.top-bar{left:0;top:0;width:1200px;height:22px;background:var(--blue)}
.header{left:0;top:22px;width:1200px;height:75px;background:var(--white)}
.brand{font-family:'Oswald',sans-serif;font-weight:500;font-size:28px;letter-spacing:1px;color:var(--blue-dark);display:flex;align-items:center;gap:8px}
.brand-dot{width:14px;height:14px;border-radius:50%;background:var(--teal)}
.nav a{position:absolute;top:50px;font-family:'Oswald',sans-serif;font-weight:300;font-size:13px;color:var(--blue);text-decoration:none}
.nav .active{border-bottom:2px solid var(--blue);padding:0 7px 5px}
.hero{left:0;top:97px;width:1200px;height:479px;background:var(--blue)}
.hero-title{left:184px;top:226px;z-index:2;font-family:'Oswald',sans-serif;font-weight:300;font-size:42px;letter-spacing:-0.3px;line-height:1.2;color:var(--white);white-space:nowrap}
.hero-title b{font-weight:500}
.hero-text{left:184px;top:310px;width:410px;font-size:13.5px;line-height:25px;color:var(--white)}
.btn{display:flex;align-items:center;justify-content:center;width:132px;height:45px;border-radius:23px;font-size:14px;text-decoration:none}
.btn-white{left:184px;top:395px;background:var(--white);color:var(--blue)}
.btn-teal{background:var(--teal);color:var(--white)}
.hero-art{left:609px;top:144px;width:460px;height:387px;border-radius:16px;background:linear-gradient(160deg,#6d8cfd,#3f62f0)}
.scroll-text{left:80px;top:335px;writing-mode:vertical-rl;transform:rotate(180deg);font-size:12px;letter-spacing:4px;color:var(--white)}
.scroll-line{left:91px;top:493px;width:1px;height:163px;background:linear-gradient(var(--white) 0 83px,#777 83px)}
.about-art{left:222px;top:681px;width:315px;height:278px;border-radius:14px;background:linear-gradient(150deg,#cfe2ff,#4f7ee0)}
.h-blue{font-family:'Oswald',sans-serif;font-weight:400;font-size:28px;color:var(--blue)}
.h-dark{font-family:'Oswald',sans-serif;font-weight:400;font-size:28px;color:var(--ink)}
.about-title{left:611px;top:666px}
.about-text{left:611px;top:735px;width:380px;font-size:14px;line-height:22.5px;color:var(--text)}
.about-text p+p{margin-top:22px}
.services{left:0;top:1073px;width:1200px;height:670px;background:var(--gray-bg)}
.services-title{left:184px;top:1256px}
.services-text{left:184px;top:1318px;width:345px;font-size:14px;line-height:25px}
.card{width:191px;height:221px;background:var(--white);padding:36px 22px 0}
.card.raised{box-shadow:0 6px 20px rgba(0,0,0,.12)}
.card-icon{width:50px;height:50px;border-radius:50%;background:var(--white);box-shadow:0 3px 12px rgba(0,0,0,.1);display:flex;align-items:center;justify-content:center;margin-left:2px}
.card h3{margin-top:26px;font-family:'Oswald',sans-serif;font-weight:400;font-size:13px;color:var(--ink)}
.card p{margin-top:12px;font-family:'Oswald',sans-serif;font-weight:300;font-size:10px;line-height:18px;color:#777}
.center{left:0;width:1200px;text-align:center}
.news-title{top:1830px}
.news-feature{left:184px;top:1932px;width:403px;height:257px;background:linear-gradient(120deg,#27b6e6,#f3f3f3 60%,#d9d9d9)}
.author{left:184px;top:2133px;width:216px;height:80px;background:var(--white);box-shadow:0 4px 14px rgba(0,0,0,.1);display:flex;align-items:center;padding-left:10px;gap:10px}
.avatar{width:32px;height:32px;border-radius:50%;background:#e6cfc0}
.author strong{display:block;font-family:'Oswald',sans-serif;font-weight:400;font-size:14px;color:var(--ink)}
.author span{font-size:9px;color:#888}
.feature-dash{left:184px;top:2248px;width:26px;height:1px;background:var(--ink)}
.feature-title{left:234px;top:2232px;width:300px;font-family:'Oswald',sans-serif;font-weight:400;font-size:14px;line-height:22px;color:var(--ink)}
.feature-text{left:234px;top:2284px;width:290px;font-size:12px;line-height:19.5px}
.feature-more{left:234px;top:2353px;font-family:'Oswald',sans-serif;font-size:12px;color:var(--ink);text-decoration:none}
.news-item{left:611px;width:400px;height:115px}
.news-thumb{position:absolute;left:0;top:0;width:119px;height:115px}
.news-item h4{position:absolute;left:143px;top:0;width:180px;font-family:'Oswald',sans-serif;font-weight:400;font-size:14px;line-height:22px;color:var(--ink)}
.news-item p{position:absolute;left:142px;top:48px;width:250px;font-size:12px;line-height:19.5px}
.clients-title{top:2455px}
.review{width:404px;height:302px;padding:20px 14px}
.review.raised{background:var(--white);box-shadow:0 6px 22px rgba(0,0,0,.1)}
.review-photo{position:absolute;left:14px;top:18px;width:106px;height:133px}
.review-name{position:absolute;left:142px;top:82px;font-family:'Oswald',sans-serif;font-weight:400;font-size:18px;color:var(--ink)}
.review-role{position:absolute;left:142px;top:112px;font-size:13px;color:var(--muted)}
.stars{position:absolute;left:142px;top:132px;font-size:16px;color:var(--gold);letter-spacing:0}
.stars .off{color:#ddd}
.quote-mark{position:absolute;left:16px;top:170px;font-family:'Oswald',sans-serif;font-size:26px;color:#ccc}
.review-text{position:absolute;left:20px;top:196px;width:364px;text-align:center;font-size:13px;line-height:22.5px;color:var(--muted)}
.dot{top:2934px;width:7px;height:7px;border-radius:50%;background:var(--blue)}
.dot.current{top:2931px;width:12px;height:12px;background:var(--white);border:2px solid var(--blue)}
.footer{left:0;top:3042px;width:1200px;height:175px;background:var(--footer)}
.footer .brand{color:var(--white)}
.footer-nav a{position:absolute;top:3101px;font-family:'Oswald',sans-serif;font-weight:400;font-size:13px;color:var(--white);text-decoration:none}
.social{top:3102px;width:16px;height:16px;border-radius:50%;border:2px solid var(--white)}
.footer-rule{left:184px;top:3179px;width:833px;height:1px;background:#666}
.footer-small{top:3191px;font-size:11px;color:#ddd;white-space:nowrap}
</style>
</head>
<body>
<div class="abs top-bar"></div>
<header class="abs header">
  <div class="abs brand" style="left:184px;top:18px"><span class="brand-dot"></span>NUVAXA</div>
</header>
<nav class="nav">
  <a class="active" href="#" style="left:758px">Home</a>
  <a href="#" style="left:825px">About Us</a>
  <a href="#" style="left:900px">Our services</a>
  <a href="#" style="left:991px">News</a>
</nav>

<section class="abs hero"></section>
<div class="abs hero-art" role="img" aria-label="Illustration of a team working on laptops beneath clouds of binary code"></div>
<h1 class="abs hero-title">Cloud-Based <b>Vaccination</b></h1>
<p class="abs hero-text">Lorem ipsum dolor sit amet, consectetur adipisicing elit, sed do eiusmod tempor incididunt ut labore.</p>
<a class="abs btn btn-white" href="#">Read More</a>
<div class="abs scroll-text">SCROLL DOWN</div>
<div class="abs scroll-line"></div>

<div class="abs about-art" role="img" aria-label="Isometric illustration of a laptop with a cloud upload and a vaccine vial with syringe"></div>
<h2 class="abs h-blue about-title">About Us</h2>
<div class="abs about-text">
  <p>Lorem ipsum dolor sit amet, consectetur adipiscing elit, sed do eiusmod tempor incididunt ut labore et dolore magna aliqua.</p>
  <p>Ut enim ad minim veniam, quis nostrud exercitation ullamco laboris nisi ut aliquip ex ea commodo consequat. Duis aute irure dolor in reprehenderit.</p>
</div>
<a class="abs btn btn-teal" href="#" style="left:611px;top:930px">Read More</a>

<section class="abs services"></section>
<h2 class="abs h-dark services-title">Our Services</h2>
<p class="abs services-text">Lorem ipsum dolor sit amet, consectetur adipisicing elit, sed do eiusmod tempor incididunt ut labore et dolore magna aliqua. Ut enim ad minim veniam, quis nostrud exercitation ullamco laboris nisi ut aliquip ex ea commodo consequat...</p>
<a class="abs btn btn-teal" href="#" style="left:184px;top:1496px">Read More</a>

<div class="abs card raised" style="left:611px;top:1164px">
  <div class="card-icon"><svg width="20" height="20" viewBox="0 0 24 24" fill="none" stroke="#4d72fb" stroke-width="2" stroke-linecap="round"><path d="M10 14a4 4 0 0 0 6 0l3-3a4 4 0 0 0-6-6l-1 1"/><path d="M14 10a4 4 0 0 0-6 0l-3 3a4 4 0 0 0 6 6l1-1"/></svg></div>
  <h3>Connect</h3>
  <p>Lorem ipsum dolor sit amet, consectetur adipisicing elit, sed do eiusmod tempor incididunt ut labore et dolore magna.</p>
</div>
<div class="abs card" style="left:825px;top:1186px">
  <div class="card-icon"><svg width="20" height="20" viewBox="0 0 24 24" fill="none" stroke="#4d72fb" stroke-width="2"><rect x="3" y="4" width="18" height="13"/><path d="M6 14l4-4 3 3 5-5"/></svg></div>
  <h3>Analystics</h3>
  <p>Lorem ipsum dolor sit amet, consectetur adipisicing elit, sed do eiusmod tempor.</p>
</div>
<div class="abs card" style="left:611px;top:1408px">
  <div class="card-icon"><svg width="20" height="20" viewBox="0 0 24 24" fill="none" stroke="#4d72fb" stroke-width="2"><rect x="3" y="4" width="18" height="12"/><path d="M9 20h6M12 16v4"/></svg></div>
  <h3>Intergration</h3>
  <p>Lorem ipsum dolor sit amet, consectetur adipisicing elit, sed do eiusmod tempor incididunt ut labore et dolore magna.</p>
</div>
<div class="abs card" style="left:825px;top:1431px">
  <div class="card-icon"><svg width="20" height="20" viewBox="0 0 24 24" fill="none" stroke="#4d72fb" stroke-width="2" stroke-linecap="round"><circle cx="12" cy="10" r="6"/><path d="M12 7v6M9 10l3-3 3 3M8 20h8"/></svg></div>
  <h3>Boost Ratio</h3>
  <p>Lorem ipsum dolor sit amet, consectetur adipisicing elit, sed do eiusmod tempor incididunt ut labore et dolore magna.</p>
</div>

<h2 class="abs h-dark center news-title">Recent news</h2>
<div class="abs news-feature" role="img" aria-label="Photo of a smiling man holding a blue speech bubble with a cloud upload symbol"></div>
<div class="abs author"><span class="avatar" role="img" aria-label="Author portrait"></span><div><strong>Owen Hale</strong><span>Founder of Ceo</span></div></div>
<div class="abs feature-dash"></div>
<h3 class="abs feature-title">Lorem ipsum dolor sit amet consectetur adipiscing. elit, sed do eiusmod</h3>
<p class="abs feature-text">Lorem ipsum dolor sit amet, consectetur adipiscing elit, sed do eiusmod tempor incididunt.ut labore et dolore magna aliqua.</p>
<a class="abs feature-more" href="#">Read More</a>

<article class="abs news-item" style="top:1932px">
  <div class="news-thumb" role="img" aria-label="Photo of a dark blue network of connected cloud icons" style="background:linear-gradient(135deg,#1c2f4f,#3c5e8c)"></div>
  <h4>Lorem ipsum dolor sit amet consectetur adipiscing.</h4>
  <p>Lorem ipsum dolor sit amet, consectetur adipiscing elit, sed do eiusmod tempor incidid unt.ut labore et dolore.</p>
</article>
<article class="abs news-item" style="top:2070px">
  <div class="news-thumb" role="img" aria-label="Photo of business people holding up a cloud sign" style="background:linear-gradient(180deg,#e9eef2,#8a8f96)"></div>
  <h4>Lorem ipsum dolor sit amet consectetur adipiscing.</h4>
  <p>Lorem ipsum dolor sit amet, consectetur adipiscing elit, sed do eiusmod tempor incidid unt.ut labore et dolore.</p>
</article>
<article class="abs news-item" style="top:2209px">
  <div class="news-thumb" role="img" aria-label="Photo of a man beside a drawn thought cloud" style="background:linear-gradient(90deg,#f4f4f4,#d9d3cc)"></div>
  <h4>Lorem ipsum dolor sit amet consectetur adipiscing.</h4>
  <p>Lorem ipsum dolor sit amet, consectetur adipiscing elit, sed do eiusmod tempor incidid unt.ut labore et dolore.</p>
</article>

<h2 class="abs h-blue center clients-title">What Our Clients Say</h2>
<div class="abs review raised" style="left:184px;top:2585px">
  <div class="review-photo" role="img" aria-label="Client portrait on an orange background" style="background:linear-gradient(160deg,#f7a823,#e88d12)"></div>
  <div class="review-name">Mira Kale</div>
  <div class="review-role">Founder of seo</div>
  <div class="stars">★★★★<span class="off">★</span></div>
  <div class="quote-mark">“</div>
  <p class="review-text">Lorem ipsum dolor sit amet, consectetur adipiscing elit, sed do eiusmod tempor incididunt ut labore et dolore magna aliqua. Ut enim ad minim veniam, quis nostrud exercitation ullamco laboris.</p>
</div>
<div class="abs review" style="left:611px;top:2585px">
  <div class="review-photo" role="img" aria-label="Client portrait in a dim street" style="background:linear-gradient(160deg,#4a4440,#2a2624)"></div>
  <div class="review-name">Theo Marsh</div>
  <div class="review-role">Founder of seo</div>
  <div class="stars">★★★★★</div>
  <div class="quote-mark">“</div>
  <p class="review-text">Lorem ipsum dolor sit amet, consectetur adipiscing elit, sed do eiusmod tempor incididunt ut labore et dolore magna aliqua. Ut enim ad minim veniam, quis nostrud exercitation ullamco laboris.</p>
</div>
<span class="abs dot current" style="left:580px"></span>
<span class="abs dot" style="left:598px"></span>
<span class="abs dot" style="left:613px"></span>

<footer class="abs footer">
  <div class="abs brand" style="left:184px;top:50px"><span class="brand-dot"></span>NUVAXA</div>
</footer>
<nav class="footer-nav">
  <a href="#" style="left:477px">Home</a>
  <a href="#" style="left:536px">About us</a>
  <a href="#" style="left:609px">Our Service</a>
  <a href="#" style="left:697px">News</a>
</nav>
<span class="abs social" style="left:889px"></span>
<span class="abs social" style="left:924px"></span>
<span class="abs social" style="left:962px"></span>
<span class="abs social" style="left:1001px"></span>
<div class="abs footer-rule"></div>
<div class="abs footer-small" style="left:184px">Privacy &amp; Policy | Trams &amp; Condition</div>
<div class="abs footer-small" style="left:737px;width:280px;text-align:right">© nuvaxa@ 2021 All Right Reserved.com</div>
</body>
</html>
```